Corporate/private aviation business needing employee recruitment flyer

We need a recruitment flyer to hand out to potential candidates with our company recruitment info on one side and advantages of a career as a Charter Pilot on the other. Need a crisp, modern look for our brand that conveys professionalism and innovation. Website: brackenwing.com.

```html
<!DOCTYPE html>
<html lang="en">
<head>
<meta charset="utf-8">
<title>Brackenwing – Charter Pilot Careers</title>
<link href="https://fonts.googleapis.com/css2?family=Poppins:ital,wght@0,400;0,600;0,800;1,800&display=swap" rel="stylesheet">
<style>
  :root {
    --page-bg: #e8ecf2;
    --paper: #ffffff;
    --brand-blue: #0d4aa8;
    --brand-blue-deep: #0a3a8f;
    --brand-blue-bright: #1a6fd6;
    --brand-yellow: #f2e400;
    --olive: rgba(150, 145, 70, 0.75);
    --lavender: rgba(160, 165, 230, 0.45);
    --ink: #2a2f3a;
    --hangar-top: #8d7f6e;
    --hangar-mid: #c9c2b8;
    --hangar-floor: #7b7f8f;
  }
  * { box-sizing: border-box; margin: 0; padding: 0; }
  html, body { width: 1200px; height: 800px; overflow: hidden; }
  body {
    background: var(--page-bg);
    font-family: "Poppins", sans-serif;
    position: relative;
  }
  .flyer {
    position: absolute;
    left: 310px; top: 25px;
    width: 580px; height: 750px;
    background: var(--paper);
    overflow: hidden;
    box-shadow: 0 6px 24px rgba(0,0,0,0.18);
  }
  .hero-photo {
    position: absolute;
    left: 42px; top: 92px;
    width: 538px; height: 240px;
    background: linear-gradient(180deg, var(--hangar-top) 0%, var(--hangar-mid) 45%, #b3acb0 70%, var(--hangar-floor) 100%);
  }
  .decor { position: absolute; left: 0; top: 0; width: 580px; height: 750px; pointer-events: none; }
  .headline {
    position: absolute;
    left: 40px; top: 350px; width: 520px;
    color: var(--brand-blue);
    font-weight: 800;
    font-size: 17.5px;
    line-height: 1.15;
    text-transform: uppercase;
  }
  .advantages {
    position: absolute;
    left: 40px; top: 408px;
    list-style: none;
    padding-left: 14px;
    border-left: 3px solid var(--brand-blue);
  }
  .advantages::after {
    content: "";
    position: absolute; left: -3px; bottom: 0;
    width: 3px; height: 48%;
    background: var(--brand-yellow);
  }
  .advantages li {
    display: flex; align-items: center; gap: 8px;
    font-size: 11.6px;
    line-height: 18.5px;
    color: var(--ink);
  }
  .tick { width: 12px; height: 12px; flex: none; }
  .footer {
    position: absolute;
    left: 0; bottom: 0;
    width: 580px; height: 150px;
    background: linear-gradient(180deg, var(--brand-blue-deep), var(--brand-blue-bright));
    color: #fff;
    padding: 18px 40px 0;
  }
  .pitch {
    font-weight: 800;
    font-size: 11.5px;
    line-height: 1.3;
    text-transform: uppercase;
    width: 300px;
  }
  .pitch em { font-style: normal; color: var(--brand-yellow); }
  .call { display: flex; align-items: center; gap: 8px; margin-top: 12px; }
  .call svg { width: 16px; height: 26px; }
  .call-label { font-weight: 800; font-size: 12.5px; line-height: 1.1; text-transform: uppercase; }
  .call-numbers { font-weight: 800; font-size: 17px; line-height: 1.1; }
  .contact-row { display: flex; gap: 22px; margin-top: 12px; font-weight: 600; font-size: 8.5px; line-height: 1.3; }
  .contact-item { display: flex; align-items: center; gap: 6px; }
  .contact-item svg { width: 13px; height: 13px; flex: none; }
  .brand-name {
    position: absolute;
    right: 36px; top: 26px;
    width: 150px;
    text-align: right;
    color: var(--brand-yellow);
    font-weight: 800;
    font-size: 15px;
    line-height: 1.15;
    text-transform: uppercase;
  }
  .brand-name span { display: block; font-size: 9px; }
  .social {
    position: absolute;
    right: 36px; top: 104px;
    display: flex; gap: 16px;
    font-size: 8px; font-weight: 400;
  }
  .social-item { display: flex; align-items: center; gap: 5px; }
  .social-dot { width: 9px; height: 9px; border-radius: 50%; background: #fff; }
</style>
</head>
<body>
  <article class="flyer">
    <div class="hero-photo" role="img" aria-label="Photo of an open aircraft hangar with private jets and turboprops parked inside under an American flag"></div>

    <svg class="decor" viewBox="0 0 580 750" aria-hidden="true">
      <polygon points="0,0 42,0 260,332 42,332 0,300" fill="var(--lavender)"/>
      <polygon points="330,42 580,0 580,72 305,92" fill="var(--olive)"/>
      <polygon points="305,92 330,42 355,88" fill="var(--brand-yellow)"/>
      <polygon points="400,60 580,40 580,280" fill="var(--lavender)"/>
      <polygon points="42,332 280,316 265,352 42,362" fill="var(--olive)"/>
      <polygon points="265,352 280,316 300,316" fill="var(--brand-yellow)"/>
    </svg>

    <h1 class="headline">Flying for an executive charter operator offers many unique advantages in your career.</h1>

    <ul class="advantages">
      <li><svg class="tick" viewBox="0 0 12 12"><circle cx="6" cy="6" r="6" fill="var(--brand-yellow)"/><path d="M3.3 6.2 5.2 8 8.8 4.3" stroke="#fff" stroke-width="1.5" fill="none"/></svg>Fly to many different, interesting destinations</li>
      <li><svg class="tick" viewBox="0 0 12 12"><circle cx="6" cy="6" r="6" fill="var(--brand-yellow)"/><path d="M3.3 6.2 5.2 8 8.8 4.3" stroke="#fff" stroke-width="1.5" fill="none"/></svg>Spend less time away from home</li>
      <li><svg class="tick" viewBox="0 0 12 12"><circle cx="6" cy="6" r="6" fill="var(--brand-yellow)"/><path d="M3.3 6.2 5.2 8 8.8 4.3" stroke="#fff" stroke-width="1.5" fill="none"/></svg>Get to spend time in other cities, see the sights, and try interesting food</li>
      <li><svg class="tick" viewBox="0 0 12 12"><circle cx="6" cy="6" r="6" fill="var(--brand-yellow)"/><path d="M3.3 6.2 5.2 8 8.8 4.3" stroke="#fff" stroke-width="1.5" fill="none"/></svg>Fly VIPs, celebrities, and high level executives</li>
      <li><svg class="tick" viewBox="0 0 12 12"><circle cx="6" cy="6" r="6" fill="var(--brand-yellow)"/><path d="M3.3 6.2 5.2 8 8.8 4.3" stroke="#fff" stroke-width="1.5" fill="none"/></svg>Get to know your passengers on a personal level</li>
      <li><svg class="tick" viewBox="0 0 12 12"><circle cx="6" cy="6" r="6" fill="var(--brand-yellow)"/><path d="M3.3 6.2 5.2 8 8.8 4.3" stroke="#fff" stroke-width="1.5" fill="none"/></svg>No dealing with unruly passengers, crowded terminals, and TSA</li>
      <li><svg class="tick" viewBox="0 0 12 12"><circle cx="6" cy="6" r="6" fill="var(--brand-yellow)"/><path d="M3.3 6.2 5.2 8 8.8 4.3" stroke="#fff" stroke-width="1.5" fill="none"/></svg>Fly a variety of aircraft and with familiar crewmembers</li>
      <li><svg class="tick" viewBox="0 0 12 12"><circle cx="6" cy="6" r="6" fill="var(--brand-yellow)"/><path d="M3.3 6.2 5.2 8 8.8 4.3" stroke="#fff" stroke-width="1.5" fill="none"/></svg>Make captain earlier and don't be just be a number on a seniority list</li>
      <li><svg class="tick" viewBox="0 0 12 12"><circle cx="6" cy="6" r="6" fill="var(--brand-yellow)"/><path d="M3.3 6.2 5.2 8 8.8 4.3" stroke="#fff" stroke-width="1.5" fill="none"/></svg>Build hands-on time in turboprop and jet aircraft instead of through instruction</li>
      <li><svg class="tick" viewBox="0 0 12 12"><circle cx="6" cy="6" r="6" fill="var(--brand-yellow)"/><path d="M3.3 6.2 5.2 8 8.8 4.3" stroke="#fff" stroke-width="1.5" fill="none"/></svg>Training at SkyCrest Training Group, the industry leader in simulator training</li>
    </ul>

    <footer class="footer">
      <p class="pitch">The airlines aren't for everyone. Consider a career path with <em>Brackenwing Aircraft as a charter pilot.</em></p>

      <div class="call">
        <svg viewBox="0 0 16 26" aria-hidden="true"><path d="M12 2 8 4c-5 5-5 13 0 18l4 2 2-5-3-2c-1.5-2-1.5-6 0-8l3-2z" fill="var(--brand-yellow)"/></svg>
        <div>
          <p class="call-label">Call us for register</p>
          <p class="call-numbers">404.555.0142, 800.555.0198</p>
        </div>
      </div>

      <div class="contact-row">
        <div class="contact-item">
          <svg viewBox="0 0 13 13" aria-hidden="true"><path d="M6.5 12S2 7.5 2 5a4.5 4.5 0 0 1 9 0c0 2.5-4.5 7-4.5 7z" fill="none" stroke="var(--brand-yellow)" stroke-width="1.4"/><circle cx="6.5" cy="5" r="1.5" fill="var(--brand-yellow)"/></svg>
          <p>Fairhaven Field (KFHV) 2210<br>Airway Circle, Atlanta, GA. 30399.</p>
        </div>
        <div class="contact-item">
          <svg viewBox="0 0 13 13" aria-hidden="true"><circle cx="6.5" cy="6.5" r="5.5" fill="none" stroke="var(--brand-yellow)" stroke-width="1.3"/><path d="M1 6.5h11M6.5 1c-3 3-3 8 0 11M6.5 1c3 3 3 8 0 11" fill="none" stroke="var(--brand-yellow)" stroke-width="1"/></svg>
          <p>hello@brackenwing.com<br>www.brackenwing.com</p>
        </div>
      </div>

      <p class="brand-name">Brackenwing Aircraft<span>&amp; Leasing Corp.</span></p>

      <div class="social">
        <div class="social-item"><span class="social-dot"></span>/company/brackenwing</div>
        <div class="social-item"><span class="social-dot"></span>/Brackenwing</div>
      </div>
    </footer>
  </article>
</body>
</html>
```